Brindle.vc needs a better website design!

We need a new and better website for Brindle.vc. We're a Canadian venture capital firm that invests in innovative entrepreneurs. We compete against the following websites: tollery.vc, quorbinvest.ca, gavelvc.com, and duskara.vc. We're a diverse group of partners and we're dedicated to the founders we invest in.
Updates

I don’t really like stock photos of random people as part of the website design…so please try to stay away from using those images. Thanks, Owen

Target Market(s)

Canadian entrepreneurs and investors

Industry/Entity Type

Venture capital, finance, investment, entrepreneurship

Coding

Coded - Design and coding required

Number of Pages Required

4 page

Font styles to use
Sans Serif

Colors

Designer to choose colors to be used in the design.

Requirements
Must have
• Clean crisp overall design. Fast and to the point.
Nice to have
• Check out www.brindle.vc - I did it myself and it is too basic and too wordy.
Should not have
• No stock images with random people in them! Not too wordy or with too many large images that are slow to load.

```html
<!DOCTYPE html>
<html lang="en">
<head>
<meta charset="utf-8">
<title>Brindle.vc — Venture Capital</title>
<link href="https://fonts.googleapis.com/css2?family=Poppins:ital,wght@0,300;0,400;0,500;0,600;1,400&display=swap" rel="stylesheet">
<style>
:root{
  --forest:#1f2b26;
  --leaf:#7b9a2f;
  --leaf-dark:#5f7a1f;
  --cream:#eef0e3;
  --mist:#eceeeb;
  --ink:#1b1f1d;
  --text:#4a4f4c;
  --line:#d9dcd8;
  --white:#ffffff;
  --stage:#f3f3f3;
}
*{margin:0;padding:0;box-sizing:border-box}
html,body{width:1200px;height:4428px;overflow:hidden}
body{background:var(--stage);font-family:'Poppins',sans-serif;color:var(--ink)}
.page{position:absolute;left:94px;top:58px;width:1010px;height:4296px;background:var(--white);box-shadow:0 20px 60px rgba(0,0,0,.12);overflow:hidden}
.abs{position:absolute}
a{color:inherit;text-decoration:none}

/* hero */
.hero-top{left:0;top:0;width:1010px;height:199px;background:var(--forest)}
.hero-left{left:0;top:0;width:226px;height:570px;background:var(--forest)}
.hero-photo{left:226px;top:199px;width:784px;height:406px;background:radial-gradient(ellipse at 60% 40%,#2f6b4a 0%,#1d4a33 45%,#0f2a1e 100%)}
.brand-badge{left:77px;top:0;width:103px;height:105px;background:var(--white);border-radius:0 0 52px 52px;display:flex;flex-direction:column;align-items:center;justify-content:center;gap:6px}
.brand-badge .dot{width:28px;height:28px;border-radius:50%;border:2px solid var(--leaf)}
.brand-name{font-size:11px;font-weight:600;color:var(--leaf);letter-spacing:.3px}
.nav{left:219px;top:45px;display:flex;gap:19px;font-size:11px;color:var(--white)}
.login{left:904px;top:45px;font-size:11px;color:var(--leaf)}
.hero-title{left:74px;top:146px;font-size:49px;font-weight:300;line-height:64px;color:var(--white);width:580px}
.hero-copy{left:75px;top:383px;font-size:10px;line-height:19px;color:#a9b1ac;width:330px}
.btn{background:var(--leaf);color:var(--white);font-size:11px;display:flex;align-items:center;justify-content:center}
.hero-btn{left:75px;top:485px;width:101px;height:31px}

/* news */
.news-label{left:75px;top:696px;font-size:15px}
.news{width:210px}
.news .date{font-size:9px;color:var(--text)}
.news .title{font-size:11px;line-height:16px;margin-top:14px;color:var(--ink)}
.news .title.hl{color:var(--leaf)}
.news .sub{font-size:10px;color:var(--text);line-height:16px}
.see-all{left:741px;top:982px;width:103px;height:29px}

/* portfolio */
.portfolio-band{left:0;top:1137px;width:1010px;height:608px;background:var(--cream)}
.fund-title{left:74px;top:1096px;font-size:43px;font-weight:400;line-height:54px}
.fund-sub{left:74px;top:1150px;font-size:40px;font-weight:300}
.card{top:1263px;width:207px;height:315px}
.card-label{top:1592px;font-size:12px;letter-spacing:1.5px}
.card .mark{position:absolute;left:16px;top:16px;font-size:14px;font-weight:600;display:flex;align-items:center;gap:6px}
.card .mark i{width:10px;height:10px;border-radius:50%;display:inline-block}
.c1{left:75px;background:linear-gradient(120deg,#f2f1ee 0%,#e3ded6 55%,#8a5a3c 100%)}
.c2{left:293px;background:linear-gradient(160deg,#3a3f3a 0%,#2a2d29 60%,#1d201d 100%);box-shadow:0 8px 20px rgba(0,0,0,.35)}
.c2 .mark{color:#8ab39d;font-weight:400;letter-spacing:4px;font-size:12px}
.c2 .blurb{position:absolute;left:12px;top:213px;width:180px;font-size:9.5px;line-height:18px;color:#e5e7e4}
.c3{left:509px;background:linear-gradient(150deg,#b9c3c8 0%,#7d8a93 50%,#3b4650 100%)}
.c3 .mark{font-weight:400;font-size:11px;color:var(--ink)}
.c4{left:726px;background:linear-gradient(150deg,#f5f6f6 0%,#d8e6ea 55%,#2a9aa6 100%)}
.c4 .mark{font-weight:400;font-size:13px;color:var(--ink)}
.view-all{left:452px;top:1659px;width:103px;height:31px;border:1px solid var(--leaf);font-size:10px;display:flex;align-items:center;justify-content:center;background:transparent}
.vc-link{left:677px;top:1668px;font-size:12px;text-decoration:underline;color:var(--ink);display:flex;align-items:center;gap:10px}
.circle-arrow{width:22px;height:22px}

/* team */
.team-bar{left:0;top:1798px;width:555px;height:81px;background:var(--forest);border-radius:0 41px 41px 0}
.team-word{left:75px;top:1820px;font-size:25px;color:var(--leaf)}
.team-kicker{left:180px;top:1818px;font-size:9px;color:var(--white)}
.team-head{left:180px;top:1832px;font-size:25px;color:var(--white)}
.team-arrow{left:457px;top:1827px}
.founder-role{left:75px;top:1934px;font-size:14px}
.founder-name{left:75px;top:1962px;font-size:28px;line-height:34px;font-weight:400}
.bio{left:75px;top:2049px;width:405px;font-size:10px;line-height:18.5px;color:var(--text)}
.bio p+p{margin-top:18px}
.portrait{width:171px;height:212px;border:1px solid var(--line)}
.p1{left:567px;top:1932px;background:linear-gradient(160deg,#4b4d49,#2d2f2c);display:flex;align-items:center;justify-content:center;color:#d8dad6;font-size:15px}
.p2{left:761px;top:1932px;background:linear-gradient(180deg,#f7f7f6,#e6e4e0)}
.p3{left:567px;top:2165px;background:linear-gradient(180deg,#f7f7f6,#e4e2de)}
.p4{left:761px;top:2165px;background:linear-gradient(180deg,#f7f7f6,#ebe6df)}

/* looking for */
.looking{left:75px;top:2484px;font-size:15px}
.looking-arrow{left:298px;top:2490px}
.phone-photo{left:75px;top:2576px;width:388px;height:456px;background:radial-gradient(ellipse at 45% 45%,#2a2c36 0%,#14151b 60%,#0a0a0d 100%)}
.traits-bg{left:463px;top:2576px;width:547px;height:456px;background:var(--mist)}
.traits-title{left:538px;top:2614px;font-size:23px;line-height:34px;font-weight:400;width:380px}
.trait{left:538px;display:flex;gap:16px;width:360px;font-size:12px;line-height:20px;color:var(--text)}
.trait .num{flex:0 0 24px;height:24px;border:1px solid var(--ink);border-radius:50%;display:flex;align-items:center;justify-content:center;font-size:12px;color:var(--ink);margin-top:2px}
.traits-link{left:538px;top:2958px;font-size:12px;line-height:18px;color:var(--leaf);text-decoration:underline;display:flex;align-items:center;gap:14px}

/* testimonial */
.says-title{left:0;top:3135px;width:1010px;text-align:center;font-size:25px}
.says-sub{left:305px;top:3178px;width:400px;text-align:center;font-size:10px;line-height:18px;color:var(--text)}
.avatar{left:469px;top:3262px;width:70px;height:70px;border-radius:50%;background:radial-gradient(circle at 50% 40%,#f0d6b9 0%,#e0b888 55%,#c8a26a 100%)}
.quote-mark{left:270px;top:3318px}
.quote{left:266px;top:3366px;width:480px;text-align:center;font-size:12px;line-height:23px;color:var(--text)}
.quote-name{left:0;top:3448px;width:1010px;text-align:center;font-size:11px;font-style:italic;color:var(--leaf);letter-spacing:.5px}
.nav-arrow{top:3371px;width:36px;height:36px}
.partner{top:3617px;width:192px;height:97px;border:1px solid var(--line);display:flex;align-items:center;justify-content:center;gap:10px;font-size:16px;font-weight:500;color:#9aa09c}
.partner i{width:18px;height:18px;background:#b9bdba;display:inline-block}
.partner .badge{width:80px;height:34px;border-radius:17px;background:#d6d9d6}

/* footer */
.footer{left:0;top:3771px;width:1010px;height:525px;background:var(--mist)}
.foot-badge{left:75px;top:3771px;width:103px;height:105px;background:var(--forest);border-radius:0 0 52px 52px;display:flex;flex-direction:column;align-items:center;justify-content:center;gap:6px}
.foot-badge .dot{width:28px;height:28px;border-radius:50%;border:2px solid var(--leaf)}
.socials{left:91px;top:3904px;display:flex;gap:10px}
.socials span{width:14px;height:14px;border-radius:50%;background:var(--ink)}
.explore{left:283px;top:3823px;font-size:20px;font-weight:500}
.foot-links{left:283px;top:3868px;font-size:21px;line-height:49px;font-weight:300;color:var(--ink);list-style:none}
.news-head{left:585px;top:3966px;font-size:19px;font-weight:500}
.email{left:585px;top:4020px;width:349px;border-bottom:1px solid #9ea39f;font-size:9px;color:var(--text);padding-bottom:6px}
.subscribe{left:585px;top:4075px;width:103px;height:31px;font-size:10px}
.legal{left:283px;top:4257px;display:flex;gap:0;font-size:10px;color:var(--text)}
.legal span:nth-child(1){width:82px}
.legal span:nth-child(2){width:74px}
.copyright{left:585px;top:4232px;width:425px;height:64px;background:var(--forest);color:var(--white);font-size:10px;display:flex;align-items:center;padding-left:20px}
</style>
</head>
<body>
<div class="page">

  <!-- Hero -->
  <div class="abs hero-top"></div>
  <div class="abs hero-left"></div>
  <div class="abs hero-photo" role="img" aria-label="Close-up of dark green palm fronds"></div>
  <div class="abs brand-badge"><span class="dot"></span><span class="brand-name">BRINDLE.VC</span></div>
  <nav class="abs nav"><a>Home</a><a>Funding</a><a>Who</a><a>What</a><a>Portfolio</a><a>Career</a><a>Contact</a></nav>
  <a class="abs login">Log in</a>
  <h1 class="abs hero-title">Invests in innovative<br>seed-stage technology<br>companies</h1>
  <p class="abs hero-copy">Brindle.vc is a venture capital firm that invests in innovative seed-stage technology companies in Western Canada focused on B2B and SaaS markets.</p>
  <a class="abs btn hero-btn">Apply</a>

  <!-- News -->
  <h2 class="abs news-label" style="font-weight:400">What's News?</h2>
  <div class="abs news" style="left:226px;top:703px"><div class="date">November 27, 2021</div><div class="title hl">New Patents for European solutions</div><div class="sub">(Lorem Metallurgical Industries )</div></div>
  <div class="abs news" style="left:487px;top:703px"><div class="date">November 27, 2021</div><div class="title">Cyber Productivity will take part in the prestigious Fintech Accelerator super charger program</div></div>
  <div class="abs news" style="left:743px;top:703px"><div class="date">November 27, 2021</div><div class="title">Congratulations to<br>Lorem Ipsum Industries for joining a great venture.</div></div>
  <div class="abs news" style="left:226px;top:881px"><div class="date">November 27, 2021</div><div class="title">New Patents for European solutions</div><div class="sub" style="font-size:9px">(Lorem Metallurgical Industries )</div></div>
  <div class="abs news" style="left:487px;top:881px"><div class="date">November 27, 2021</div><div class="title">Lorem Venture partners with<br>Launch Hub Poland</div></div>
  <div class="abs news" style="left:743px;top:881px"><div class="date">November 27, 2021</div><div class="title">Pre-Lorem testing presentation in UK</div></div>
  <a class="abs btn see-all" style="font-size:10px">See All</a>

  <!-- Portfolio -->
  <div class="abs portfolio-band"></div>
  <h2 class="abs fund-title">Brindle Fund I</h2>
  <h3 class="abs fund-sub">Portfolio Companies</h3>

  <div class="abs card c1" role="img" aria-label="Person in a suit carrying a leather briefcase"><span class="mark"><i style="background:var(--ink)"></i>Kestrun</span></div>
  <div class="abs card c2"><span class="mark">TIDEWELL</span><p class="blurb">Brindle.vc is a venture capital firm that invests in innovative seed-stage technology companies in Western Canada focused on B2B and SaaS markets.</p></div>
  <div class="abs card c3" role="img" aria-label="Smartphone home screen with app icons"><span class="mark"><i style="border:1.5px solid var(--ink)"></i>Lockfield</span></div>
  <div class="abs card c4" role="img" aria-label="Smartphone resting on a laptop"><span class="mark">Plainly <i style="background:#2a6b5a"></i></span></div>
  <div class="abs card-label" style="left:75px">KESTRUN</div>
  <div class="abs card-label" style="left:293px">TIDEWELL</div>
  <div class="abs card-label" style="left:509px">LOCKFIELD</div>
  <div class="abs card-label" style="left:726px">PLAINLY</div>
  <a class="abs view-all">View All</a>
  <a class="abs vc-link">How We Make Our VC Investments
    <svg class="circle-arrow" viewBox="0 0 22 22"><circle cx="11" cy="11" r="10" fill="none" stroke="#7b9a2f" stroke-width="1.3"/><path d="M7 11h8M12 8l3 3-3 3" fill="none" stroke="#7b9a2f" stroke-width="1.3"/></svg></a>

  <!-- Team -->
  <div class="abs team-bar"></div>
  <div class="abs team-word">Team</div>
  <div class="abs team-kicker">Behind Brindle Capital</div>
  <div class="abs team-head">Respected Leaders</div>
  <svg class="abs team-arrow circle-arrow" viewBox="0 0 22 22"><circle cx="11" cy="11" r="10" fill="none" stroke="#7b9a2f" stroke-width="1.3"/><path d="M7 11h8M12 8l3 3-3 3" fill="none" stroke="#7b9a2f" stroke-width="1.3"/></svg>

  <div class="abs founder-role">Founder Brindle.vc</div>
  <h2 class="abs founder-name">Owen Benning<br>General Partner, Funds I and II</h2>
  <div class="abs bio">
    <p>Owen is an experienced entrepreneur and successful investor. He started Forgeline.co, an executive mentoring and business coaching firm. He also founded and led four investor-backed, technology startups in Silicon Valley, California over a 20-year period. In addition to managing strategy, business development, and finance, Owen raised over $100 million in venture capital funding for his startups and others he advised. Over the years, he has worked for several private equity and venture capital firms.</p>
    <p>Owen is a member of the entrepreneurial North100 group, an angel investor with Tallgrass Angels, a mentor with the Founder Mentoring Circle group of the Prairie University, and founder of the Pitchmeet.org emerging-technology pitch event.</p>
    <p>Owen has a BA in Economics from Eastbrook University and an MBA from Westvale University, where he focused on leadership and entrepreneurship. Between his time at Eastbrook and Westvale, he played professional ice hockey in Europe and traveled extensively throughout the world.</p>
  </div>
  <div class="abs portrait p1" role="img" aria-label="Portrait of Owen Benning">Owen Benning</div>
  <div class="abs portrait p2" role="img" aria-label="Illustrated portrait of a partner"></div>
  <div class="abs portrait p3" role="img" aria-label="Illustrated portrait of a partner"></div>
  <div class="abs portrait p4" role="img" aria-label="Illustrated portrait of a partner"></div>

  <!-- Looking for -->
  <div class="abs looking">What we are looking for?</div>
  <svg class="abs looking-arrow" width="20" height="20" viewBox="0 0 20 20"><path d="M3 5h9v10M8 11l4 4 4-4" fill="none" stroke="#7b9a2f" stroke-width="1.4"/></svg>
  <div class="abs phone-photo" role="img" aria-label="Smartphone showing a stock market trading app"></div>
  <div class="abs traits-bg"></div>
  <h2 class="abs traits-title">We invest in innovative<br>technology companies<br>with these characteristics</h2>
  <div class="abs trait" style="top:2736px"><span class="num">1</span><span>Founding Team: Visionary, Committed, Coachable, Skilled, Aligned, With Market Fit</span></div>
  <div class="abs trait" style="top:2794px"><span class="num">2</span><span>Total Addressable Market: Large, Growing, and Attractive; With a Manageable Competitive Landscape</span></div>
  <div class="abs trait" style="top:2871px"><span class="num">3</span><span>Product Market Fit: MVP + Initial Market Validation; Early Revenue and Growth Potential</span></div>
  <a class="abs traits-link"><span>Other things we consider in evaluating<br>our venture capital investments</span>
    <svg class="circle-arrow" viewBox="0 0 22 22"><circle cx="11" cy="11" r="10" fill="none" stroke="#7b9a2f" stroke-width="1.3"/><path d="M7 11h8M12 8l3 3-3 3" fill="none" stroke="#7b9a2f" stroke-width="1.3"/></svg></a>

  <!-- Testimonial -->
  <h2 class="abs says-title" style="font-weight:400">What our client says</h2>
  <p class="abs says-sub">Lorem ipsum dolor sit amet, consetetur sadipscing elitr, sed diam nonumy eirmod tempor invidunt ut labore et dolore magna aliquyam erat,</p>
  <div class="abs avatar" role="img" aria-label="Client portrait"></div>
  <svg class="abs quote-mark" width="40" height="30" viewBox="0 0 40 30"><path d="M2 28V16C2 8 6 3 14 1l2 4c-4 2-6 5-6 9h7v14zM22 28V16c0-8 4-13 12-15l2 4c-4 2-6 5-6 9h7v14z" fill="#a9bd7a"/></svg>
  <p class="abs quote">Lorem ipsum dolor sit amet, consetetur sadipscing elitr, sed diam nonumy eirmod tempor invidunt ut labore et dolore magna aliquyam erat, sed diam voluptua. At vero eos et accusam et</p>
  <div class="abs quote-name">LENA MARSH</div>
  <svg class="abs nav-arrow" style="left:145px" viewBox="0 0 36 36"><circle cx="18" cy="18" r="18" fill="#1f2b26"/><path d="M20 12l-6 6 6 6" fill="none" stroke="#fff" stroke-width="1.6"/></svg>
  <svg class="abs nav-arrow" style="left:827px" viewBox="0 0 36 36"><circle cx="18" cy="18" r="18" fill="#1f2b26"/><path d="M16 12l6 6-6 6" fill="none" stroke="#fff" stroke-width="1.6"/></svg>

  <div class="abs partner" style="left:98px"><span class="badge"></span></div>
  <div class="abs partner" style="left:305px"><i></i>Halden</div>
  <div class="abs partner" style="left:511px"><i style="border-radius:50%"></i>Corvent</div>
  <div class="abs partner" style="left:718px;letter-spacing:3px;font-weight:400"><i></i>MERIDA</div>

  <!-- Footer -->
  <div class="abs footer"></div>
  <div class="abs foot-badge"><span class="dot"></span><span class="brand-name">BRINDLE.VC</span></div>
  <div class="abs socials"><span></span><span></span><span></span><span></span></div>
  <h3 class="abs explore">Explore Brindle.vc</h3>
  <ul class="abs foot-links"><li>Home</li><li>Funding</li><li>Who</li><li>What</li><li>Portfolio</li><li>Career</li><li>Contact</li></ul>
  <h3 class="abs news-head">Join to Our Newsletter</h3>
  <div class="abs email">Enter your mail</div>
  <a class="abs btn subscribe">Subscribe</a>
  <div class="abs legal"><span>Privacy</span><span>Legal</span><span>Terms &amp; Conditions</span></div>
  <div class="abs copyright">©&nbsp;&nbsp;Copyright 2021, All Rights Reserved</div>
</div>
</body>
</html>
```